Business Card Design - Service Company

Use of the card mainly in living rooms and relations b2b We wish a card with a modern design, blue tones in the background would be a plus The card must be front / back (one side with the logo / the other with the information of contact )

Font styles to use
Serif

Requirements
Must have
• Using the map on the back of the business card Editable format! Photoshop CS2 / Illustrator CS2
Nice to have
• Maquis Vertex IT Pierre Blanche Commercial Center, 20480 Lorvanu 0495718243 Siret 71384096200018 APE 6203Y https://www.fb.com/ateliertech.maquisvertex www.maquis-vertex.com

```html
<!DOCTYPE html>
<html lang="fr">
<head>
<meta charset="utf-8">
<title>Maquis Vertex IT – Business Card</title>
<link rel="stylesheet" href="https://fonts.googleapis.com/css2?family=Roboto:wght@400;500;700&display=swap">
<style>
  :root {
    --backdrop: #161616;
    --card: #222223;
    --card-edge: #2c2c2d;
    --brand-blue: #2a8fd4;
    --steel: #8d8f92;
    --ink-light: #f2f2f2;
    --ink-dim: #cfcfcf;
  }
  * { box-sizing: border-box; margin: 0; padding: 0; }
  html, body {
    width: 1200px;
    height: 900px;
    overflow: hidden;
    background: var(--backdrop);
    font-family: "Roboto", Arial, sans-serif;
  }
  .sheet {
    position: relative;
    width: 1200px;
    height: 900px;
  }
  .card {
    position: absolute;
    left: 240px;
    width: 720px;
    height: 410px;
    background: linear-gradient(135deg, var(--card) 0%, var(--card) 55%, var(--card-edge) 100%);
    box-shadow: 0 10px 30px rgba(0,0,0,.6);
  }
  .card--front { top: 25px; }
  .card--back { top: 465px; }

  /* front */
  .front-mark {
    position: absolute;
    left: 0; right: 0; top: 150px;
    display: flex;
    justify-content: center;
    align-items: center;
    gap: 16px;
  }
  .brand-name {
    font-weight: 700;
    font-size: 40px;
    letter-spacing: 1px;
    text-transform: uppercase;
    line-height: 1;
  }
  .front-mark .brand-name { color: var(--steel); }
  .brand-square {
    width: 22px; height: 22px;
    background: var(--steel);
  }
  .legal-line {
    position: absolute;
    left: 0; right: 0; bottom: 28px;
    text-align: center;
    color: var(--ink-light);
    font-size: 17px;
    font-weight: 500;
  }

  /* back */
  .back-mark {
    position: absolute;
    left: 40px; top: 180px;
    width: 300px;
    display: flex;
    align-items: center;
    gap: 12px;
  }
  .back-mark .brand-name { color: var(--brand-blue); font-size: 32px; }
  .back-mark .brand-square { background: var(--brand-blue); width: 18px; height: 18px; }
  .divider {
    position: absolute;
    left: 365px; top: 90px;
    width: 2px; height: 215px;
    background: var(--brand-blue);
  }
  .contact {
    position: absolute;
    left: 395px; top: 95px;
    color: var(--ink-light);
  }
  .contact__name {
    color: var(--brand-blue);
    font-size: 30px;
    font-weight: 500;
    letter-spacing: 2px;
    text-transform: uppercase;
  }
  .contact__role {
    font-size: 19px;
    font-weight: 500;
    margin-top: 2px;
  }
  .contact__address {
    font-size: 19px;
    font-weight: 500;
    line-height: 1.35;
    margin-top: 16px;
  }
  .contact__list {
    list-style: none;
    margin-top: 14px;
    font-size: 19px;
    font-weight: 500;
    line-height: 1.5;
  }
  .contact__list li { display: flex; align-items: center; gap: 10px; }
  .contact__list svg { width: 14px; height: 14px; flex: none; }
  .dot { width: 10px; height: 10px; border-radius: 50%; background: var(--brand-blue); margin: 0 2px; flex: none; }
</style>
</head>
<body>
<main class="sheet">
  <section class="card card--front" aria-label="Card front">
    <div class="front-mark">
      <span class="brand-name">Maquis Vertex IT</span>
      <span class="brand-square"></span>
    </div>
    <p class="legal-line">Siret 71384096200018 APE 6203Y</p>
  </section>

  <section class="card card--back" aria-label="Card back">
    <div class="back-mark">
      <span class="brand-name">Maquis Vertex IT</span>
      <span class="brand-square"></span>
    </div>
    <div class="divider"></div>
    <div class="contact">
      <p class="contact__name">Lucien Moretti</p>
      <p class="contact__role">Director</p>
      <p class="contact__address">Centre Commercial<br>Pierre Blanche, 20480 Lorvanu</p>
      <ul class="contact__list">
        <li>
          <svg viewBox="0 0 24 24" aria-hidden="true"><path fill="#2a8fd4" d="M6.6 10.8a15.5 15.5 0 0 0 6.6 6.6l2.2-2.2a1 1 0 0 1 1-.25 11.4 11.4 0 0 0 3.6.57 1 1 0 0 1 1 1V20a1 1 0 0 1-1 1A17 17 0 0 1 3 4a1 1 0 0 1 1-1h3.5a1 1 0 0 1 1 1c0 1.25.2 2.45.57 3.57a1 1 0 0 1-.25 1z"/></svg>
          0495718243
        </li>
        <li>
          <svg viewBox="0 0 24 24" aria-hidden="true" fill="none" stroke="#2a8fd4" stroke-width="2"><circle cx="12" cy="12" r="9"/><path d="M3 12h18M12 3c3 3 3 15 0 18M12 3c-3 3-3 15 0 18"/></svg>
          www.maquis-vertex.com
        </li>
        <li>
          <span class="dot"></span>
          /ateliertech.maquisvertex
        </li>
      </ul>
    </div>
  </section>
</main>
</body>
</html>
```